ROVA Pty Ltd Business Card

Looking for a simple yet eye-catching double-sided business card design using my company logo on one side and contact details on the other.

Target Market(s)

Government

Industry/Entity Type

Communication Systems Engineering

Contact Information for Business Card

ROVA Pty Ltd

Requirements
Nice to have
• Would be great to have a QR code so details can be scanned into contacts

```html
<!DOCTYPE html>
<html lang="en">
<head>
<meta charset="utf-8">
<title>ROVA Pty Ltd Business Card</title>
<link href="https://fonts.googleapis.com/css2?family=Arimo:wght@400;700&display=swap" rel="stylesheet">
<style>
  :root {
    --backdrop: #2b2b2d;
    --card: #333b44;
    --card-edge: #3a434c;
    --ink-light: #f4f5f6;
    --ink-soft: #d5d9dd;
    --panel: #f3f4f5;
    --trace-dark: rgba(200, 206, 212, 0.30);
    --trace-light: rgba(40, 46, 52, 0.22);
  }
  * { box-sizing: border-box; margin: 0; padding: 0; }
  html, body {
    width: 1200px;
    height: 689px;
    overflow: hidden;
    background: var(--backdrop);
    font-family: "Arimo", Arial, sans-serif;
  }
  .canvas {
    position: relative;
    width: 1200px;
    height: 689px;
    display: flex;
    align-items: center;
    justify-content: center;
    gap: 50px;
  }
  .card {
    position: relative;
    width: 520px;
    height: 298px;
    border-radius: 16px;
    background: var(--card);
    border: 1px solid var(--card-edge);
    overflow: hidden;
    color: var(--ink-light);
  }

  /* Front side */
  .card-front {
    display: flex;
    align-items: center;
    justify-content: center;
    gap: 22px;
  }
  .brand-dot {
    width: 64px;
    height: 64px;
    border-radius: 50%;
    border: 3px solid var(--ink-light);
  }
  .brand-name {
    font-weight: 700;
    font-size: 58px;
    letter-spacing: 4px;
    color: var(--ink-light);
  }

  /* Back side */
  .back-panel {
    position: absolute;
    inset: 0;
    width: 100%;
    height: 100%;
  }
  .back-panel .panel-shape { fill: var(--panel); }
  .circuit-tree {
    position: absolute;
    left: 270px;
    top: 14px;
    width: 240px;
    height: 270px;
    border-radius: 50% 50% 40% 40%;
    background:
      radial-gradient(ellipse at 70% 40%, var(--trace-light), rgba(40,46,52,0) 60%),
      radial-gradient(ellipse at 35% 55%, var(--trace-dark), rgba(200,206,212,0) 62%);
  }
  .back-brand {
    position: absolute;
    left: 36px;
    top: 52px;
    font-weight: 700;
    font-size: 40px;
    letter-spacing: 3px;
  }
  .details {
    position: absolute;
    left: 36px;
    top: 124px;
  }
  .person-name {
    font-weight: 700;
    font-size: 19px;
  }
  .person-role {
    font-size: 11px;
    color: var(--ink-soft);
    margin-top: 2px;
  }
  .address {
    margin-top: 14px;
    font-size: 13px;
    line-height: 1.3;
    color: var(--ink-soft);
  }
  .contact-list {
    list-style: none;
    margin-top: 12px;
    font-size: 13px;
    line-height: 1.35;
    color: var(--ink-soft);
  }
  .contact-list li {
    display: flex;
    align-items: center;
    gap: 8px;
  }
  .contact-list svg {
    width: 11px;
    height: 11px;
    fill: var(--ink-light);
    flex: none;
  }
</style>
</head>
<body>
<main class="canvas">
  <section class="card card-front" aria-label="Business card front">
    <span class="brand-dot"></span>
    <span class="brand-name">ROVA</span>
  </section>

  <section class="card card-back" aria-label="Business card back">
    <svg class="back-panel" viewBox="0 0 520 298" preserveAspectRatio="none" aria-hidden="true">
      <polygon class="panel-shape" points="395,0 520,0 520,298 470,298 470,228 456,214 456,152 424,122 424,74 398,50 398,20 380,20 380,0"/>
    </svg>
    <div class="circuit-tree" role="img" aria-label="Circuit board tree illustration spreading across the dark card and white panel"></div>

    <div class="back-brand">ROVA</div>

    <div class="details">
      <div class="person-name">Daniel Morgan</div>
      <div class="person-role">Managing Director</div>
      <div class="address">214 Harbour Street<br>Wellington Bay, 30418</div>
      <ul class="contact-list">
        <li>
          <svg viewBox="0 0 12 12" aria-hidden="true"><path d="M2.5 1h2l1 2.8-1.3 1a6 6 0 0 0 2.9 2.9l1-1.3 2.9 1v2A1.2 1.2 0 0 1 9.8 11 8.8 8.8 0 0 1 1 2.2 1.2 1.2 0 0 1 2.5 1z"/></svg>
          555-012-4478
        </li>
        <li>
          <svg viewBox="0 0 12 12" aria-hidden="true"><path d="M1 2.5h10v7H1z M1.6 3l4.4 3.4L10.4 3" stroke="#333b44" stroke-width="0.9"/></svg>
          info@rovacomms.org
        </li>
        <li>
          <svg viewBox="0 0 12 12" aria-hidden="true"><circle cx="6" cy="6" r="5"/><path d="M1 6h10M6 1c2 2.6 2 7.4 0 10M6 1c-2 2.6-2 7.4 0 10" stroke="#333b44" stroke-width="0.8" fill="none"/></svg>
          www.rovacomms.org
        </li>
      </ul>
    </div>
  </section>
</main>
</body>
</html>
```